MARBLED SPARROW WEB DESIGN PROJECT

We are a brand new company called "Marbled Sparrow" which specialise in one-off Vintage Clothing. We would like somebody to design a web page which will be the sole income for our company. Our main aim is to have an easy searchable website which is user friendly. The key to the website is to target people who do not like the idea of op-shopping but love vintage clothes - this website will be the answer.
Updates

This website will need to be coded to work with Tin Lantern - Please read this before you start. https://help.tinlantern.example/articles/Public/How-do-I-create-custom-template-files-for-my-store

Hi everyone, Just want to make note that the this website is for young people. Just so people a clear I want modern young people dressed in Vintage clothes as this is that reality and what they would like to see. Not people dressed like they are going to a fancy dress party, i.e. dresses like it was that era. Thanks Mirela

Coding

Coded - Design and coding required

```html
<!DOCTYPE html>
<html lang="en">
<head>
<meta charset="utf-8">
<title>Marbled Sparrow – Vintage Clothing</title>
<link href="https://fonts.googleapis.com/css2?family=Open+Sans:wght@400;600;700&family=Alike&family=Patrick+Hand+SC&display=swap" rel="stylesheet">
<style>
:root{
  --green:#6aaa3a;
  --green-dark:#4f8a26;
  --navy:#133a66;
  --ink:#3a3a3a;
  --muted:#666;
  --line:#d6d6d6;
  --footer:#f2f2f2;
  --white:#fff;
  --serif:"Alike", Georgia, serif;
  --hand:"Patrick Hand SC", cursive;
  --sans:"Open Sans", Arial, sans-serif;
}
*{box-sizing:border-box;margin:0;padding:0}
html,body{width:740px;height:1200px;overflow:hidden;background:var(--white)}
body{position:relative;font-family:var(--sans);color:var(--ink)}
.abs{position:absolute}
a{color:inherit;text-decoration:none}

/* header */
.brand{left:71px;top:12px;font-family:var(--hand);font-size:30px;line-height:26px;color:var(--green);letter-spacing:2px}
.account{right:73px;top:17px;font-family:var(--serif);font-size:9px;color:var(--navy);letter-spacing:.5px}
.account span{margin:0 8px;color:var(--muted)}
.cart{right:73px;top:41px;font-family:var(--serif);font-size:9px;color:var(--navy);display:flex;align-items:center;gap:6px}

/* nav */
.nav{left:0;top:75px;width:740px;height:27px;border-top:1px dashed #999;border-bottom:1px dashed #999;}
.nav ul{list-style:none;display:flex;position:absolute;left:71px;top:0;height:25px}
.nav li{font-family:var(--serif);font-size:10px;color:#555;padding:0 18px;line-height:25px;border-right:1px solid var(--line)}
.nav li:first-child{padding-left:0;color:var(--navy)}
.search{position:absolute;left:540px;top:0;width:128px;height:25px;border-right:1px solid #999;font-family:var(--serif);font-size:9px;color:#888;line-height:25px;padding-left:16px}
.search svg{position:absolute;right:6px;top:6px}

/* hero */
.hero{left:0;top:102px;width:740px;height:283px;background:linear-gradient(90deg,#6e6550 0%,#4b4534 45%,#3a3628 70%,#2c2a20 100%)}
.hero-title{left:378px;top:148px;font-family:var(--hand);font-size:40px;color:var(--green);letter-spacing:3px}
.hero-sub{left:376px;top:196px;font-family:var(--hand);font-size:28px;line-height:25px;color:var(--white);letter-spacing:2px}
.badge{left:412px;top:262px;width:98px;height:98px;border-radius:50%;background:var(--green);display:flex;align-items:center;justify-content:center}
.badge div{width:78px;height:78px;border-radius:50%;background:#1b1b1b;border:3px solid var(--white);color:var(--white);font-family:var(--hand);font-size:20px;line-height:18px;text-align:center;display:flex;align-items:center;justify-content:center;transform:rotate(-30deg)}
.shop{left:587px;top:276px;width:55px;height:55px;border-radius:50%;background:var(--green);border:2px solid var(--green-dark);color:var(--white);font-family:var(--hand);font-size:14px;line-height:12px;text-align:center;display:flex;align-items:center;justify-content:center}

/* feature products */
.section-title{left:71px;top:405px;font-family:var(--serif);font-size:14px;color:var(--navy);letter-spacing:.5px}
.section-rule{left:71px;top:426px;width:570px;border-top:1px dashed #aaa}
.section-rule::before{content:"";position:absolute;left:0;top:-2px;width:62px;border-top:2px solid var(--navy)}
.arrows{left:644px;top:421px}
.card{position:absolute;width:137px;height:160px;border:1px solid var(--line);background:var(--white);text-align:center}
.card .photo{height:113px}
.card .name{font-size:9px;margin-top:10px;color:var(--ink)}
.card .price{font-size:11px;font-weight:700;color:var(--navy);margin-top:5px}
.card.active{border-color:var(--navy)}
.card.active .info{background:var(--navy);height:45px;padding-top:1px}
.card.active .name,.card.active .price{color:var(--white)}
.card .hover-icon{position:absolute;left:54px;top:42px;width:30px;height:30px;border-radius:50%;background:var(--navy);display:flex;align-items:center;justify-content:center}

/* promo banners */
.promo{position:absolute;top:803px;width:185px;height:128px;border-radius:3px;overflow:hidden}
.promo .label{position:absolute;left:0;bottom:0;width:100%;height:31px;font-family:var(--hand);font-size:18px;color:var(--white);line-height:31px;text-align:right;padding-right:12px;letter-spacing:1px}

/* slogan */
.slogan{left:71px;top:955px;width:597px;height:50px;background:var(--navy);color:var(--white);font-family:var(--hand);font-size:12px;line-height:18px;text-align:center;padding-top:7px;letter-spacing:1px;border-radius:3px}
.leaf{position:absolute;top:952px;width:54px;height:52px;border-radius:50% 50% 40% 40%;background:var(--green)}

/* footer */
.footer{left:0;top:1029px;width:740px;height:136px;background:var(--footer)}
.col{position:absolute;top:1045px}
.col h4{font-family:var(--serif);font-weight:400;font-size:10px;color:var(--navy);letter-spacing:.5px;padding-bottom:6px;border-bottom:1px solid var(--line);width:78px;white-space:nowrap}
.col ul{list-style:none;margin-top:6px}
.col li{font-size:7.5px;line-height:15px;color:#555}
.col li b{font-weight:400;display:inline-block;width:66px}
.divider{position:absolute;top:1045px;height:120px;border-left:1px solid #9aa}
.news p{font-size:7.5px;line-height:12px;color:#555;width:158px;margin-top:8px}
.news .field{margin-top:8px;width:158px;height:22px;background:var(--white);border:1px solid var(--line);font-size:7.5px;line-height:20px;padding-left:8px;color:#555;position:relative}
.news .field i{position:absolute;right:-1px;top:-1px;width:23px;height:22px;background:var(--green)}
.news .field i::after{content:"";position:absolute;left:9px;top:6px;border-left:6px solid var(--white);border-top:5px solid transparent;border-bottom:5px solid transparent}
.social{display:flex;gap:0;margin-top:10px}
.social span{width:35px;height:14px;border-right:1px solid var(--line);display:flex;align-items:center;justify-content:center}
.social span:last-child{border:0}
.social span i{width:9px;height:9px;border-radius:50%;background:#9aa3ad}
.social span:first-child i{background:var(--navy)}

.bottom{left:0;top:1165px;width:740px;height:35px;background:var(--navy)}
.pay{position:absolute;left:71px;top:11px;display:flex;gap:5px}
.pay i{width:22px;height:14px;border-radius:2px;background:#dcdcdc}
.copy{position:absolute;right:72px;top:13px;font-size:7.5px;color:#b8c4d4}
.copy b{color:var(--white);font-weight:400}
</style>
</head>
<body>

<header>
  <div class="abs brand">MARBLED<br>SPARROW</div>
  <div class="abs account"><a href="#">LOGIN</a><span>/</span><a href="#">REGISTER</a></div>
  <div class="abs cart">
    <svg width="14" height="13" viewBox="0 0 14 13"><path d="M1 1h2l2 7h6l2-5H4" fill="none" stroke="#6aaa3a" stroke-width="1.5"/><circle cx="6" cy="11" r="1.2" fill="#6aaa3a"/><circle cx="10" cy="11" r="1.2" fill="#6aaa3a"/></svg>
    CART ITEM (0) ▾
  </div>
</header>

<nav class="abs nav">
  <ul>
    <li>HOME</li><li>WOMEN</li><li>MEN</li><li>STYLE TIPS</li><li>FAQS</li><li>CONTACT US</li><li>SALE</li>
  </ul>
  <div class="search">Search
    <svg width="12" height="12" viewBox="0 0 12 12"><circle cx="7" cy="5" r="3.5" fill="none" stroke="#6aaa3a" stroke-width="1.6"/><path d="M4.5 7.5L1 11" stroke="#6aaa3a" stroke-width="2"/></svg>
  </div>
</nav>

<section>
  <div class="abs hero" role="img" aria-label="Woman in a wide-brimmed hat and black dress beside a vintage car"></div>
  <div class="abs hero-title">FALL SALE</div>
  <div class="abs hero-sub">NEW DELAS FOR<br>THE NEW SEASON</div>
  <div class="abs badge"><div>50%<br>OFF</div></div>
  <div class="abs shop">SHOP<br>NOW</div>
</section>

<section>
  <h2 class="abs section-title">Feature Products</h2>
  <div class="abs section-rule"></div>
  <svg class="abs arrows" width="24" height="10" viewBox="0 0 24 10"><path d="M0 5l5-4v2.5h5v3H5V9z" fill="#999"/><path d="M24 5l-5-4v2.5h-5v3h5V9z" fill="#6aaa3a"/></svg>

  <div class="card active" style="left:71px;top:442px">
    <div class="photo" role="img" aria-label="Young woman in sunglasses sitting outdoors" style="background:linear-gradient(#c9cbd1,#b9b3aa)"></div>
    <div class="hover-icon"><svg width="14" height="13" viewBox="0 0 14 13"><path d="M1 1h2l2 7h6l2-5H4" fill="none" stroke="#fff" stroke-width="1.5"/><circle cx="6" cy="11" r="1.2" fill="#fff"/><circle cx="10" cy="11" r="1.2" fill="#fff"/></svg></div>
    <div class="info"><div class="name">Lorem ipsum dolor sit</div><div class="price">$265.15</div></div>
  </div>
  <div class="card" style="left:224px;top:442px"><div class="photo" role="img" aria-label="Woman in black dress and hat by a wooden wall" style="background:linear-gradient(#8a6a4a,#3a2c22)"></div><div class="name">Lorem ipsum dolor sit</div><div class="price">$265.15</div></div>
  <div class="card" style="left:377px;top:442px"><div class="photo" role="img" aria-label="Woman in grey lace dress against a stone wall" style="background:linear-gradient(#8a8580,#5c5650)"></div><div class="name">Lorem ipsum dolor sit</div><div class="price">$265.15</div></div>
  <div class="card" style="left:530px;top:442px"><div class="photo" role="img" aria-label="Woman in a blue floral dress on a city street" style="background:linear-gradient(#7a6a62,#3e6a8a)"></div><div class="name">Lorem ipsum dolor sit</div><div class="price">$265.15</div></div>

  <div class="card" style="left:71px;top:618px"><div class="photo" role="img" aria-label="Woman in white shirt and black waistcoat" style="background:linear-gradient(#e6e6e6,#8c8c8c)"></div><div class="name">Lorem ipsum dolor sit</div><div class="price">$265.15</div></div>
  <div class="card" style="left:224px;top:618px"><div class="photo" role="img" aria-label="Woman in a peach dress at a railway station" style="background:linear-gradient(#8a8a86,#d8b8a4)"></div><div class="name">Lorem ipsum dolor sit</div><div class="price">$265.15</div></div>
  <div class="card" style="left:377px;top:618px"><div class="photo" role="img" aria-label="Woman in a black strapless dress" style="background:linear-gradient(#d2d2d2,#9a9a9a)"></div><div class="name">Lorem ipsum dolor sit</div><div class="price">$265.15</div></div>
  <div class="card" style="left:530px;top:618px"><div class="photo" role="img" aria-label="Red-haired woman with glasses in a gingham top" style="background:linear-gradient(#c9a38a,#e8d6a0)"></div><div class="name">Lorem ipsum dolor sit</div><div class="price">$265.15</div></div>
</section>

<section>
  <div class="promo" style="left:71px" role="img" aria-label="Group of friends in sunglasses smiling" >
    <div style="height:100%;background:linear-gradient(#e8d070,#c09070)"></div>
    <div class="label" style="background:rgba(19,58,102,.92)">STYLE TIPS</div>
  </div>
  <div class="promo" style="left:277px" role="img" aria-label="Women in headscarves and colourful bangles in a car">
    <div style="height:100%;background:linear-gradient(#a8b070,#5a6a3a)"></div>
    <div class="label" style="background:rgba(106,170,58,.92)">SHOP ERA</div>
  </div>
  <div class="promo" style="left:483px" role="img" aria-label="Woman in a hat beside a vintage car">
    <div style="height:100%;background:linear-gradient(#6a5a44,#2e2a22)"></div>
    <div class="label" style="background:rgba(196,22,30,.95);font-size:13px">JOIN OUR VIP CLUB 20 % OFF</div>
  </div>
</section>

<section>
  <div class="abs slogan">MARBLED SPARROW IS ALL ABOUT BEING DIFFERENT. THAT'S WAY ALL<br>OUR CLOTHES ARE UNIQUE, SO YOU CAN BE DAZZLING DIFFERENT</div>
  <div class="leaf" style="left:71px" role="img" aria-label="Green leaf ornament"></div>
  <div class="leaf" style="left:616px" role="img" aria-label="Green leaf ornament"></div>
</section>

<footer>
  <div class="abs footer"></div>
  <div class="col" style="left:71px"><h4 style="width:100px">MARBLED SPARROW</h4>
    <ul><li style="color:var(--navy)">Home</li><li>About Us</li><li>Terms of use</li><li>Privacy Policy</li><li>Press</li><li>Contact Us</li></ul></div>
  <div class="divider" style="left:195px"></div>
  <div class="col" style="left:222px"><h4 style="width:78px">CONNECT WITH US</h4>
    <ul><li>My Account</li><li>Style Tips</li><li>FAQs</li><li>Shipping</li><li>Track Your Order</li><li>Size Chart</li></ul></div>
  <div class="divider" style="left:338px"></div>
  <div class="col" style="left:366px"><h4 style="width:92px">CONNECT WITH US</h4>
    <ul><li><b>Men</b>50S</li><li><b>Women</b>60S</li><li><b>Accessories</b>70S</li><li><b>Bags</b>80S</li><li><b>Shoes</b>90S</li></ul></div>
  <div class="divider" style="left:481px"></div>
  <div class="col news" style="left:509px"><h4 style="width:158px">NEWSLETTER</h4>
    <p>Lorem ipsum dolor sit amet, consr adipi scing elit. Aliquam</p>
    <div class="field">you@inbox.example<i></i></div>
    <div class="social"><span><i></i></span><span><i></i></span><span><i></i></span><span><i></i></span><span><i></i></span></div>
  </div>

  <div class="abs bottom">
    <div class="pay"><i></i><i></i><i></i><i></i><i></i><i></i></div>
    <div class="copy">Copyright © 2015 <b>Marbled Sparrow</b>.</div>
  </div>
</footer>

</body>
</html>
```